Evergrove Yard Service and Beyond LLC

• Mowing
• Weed eating
•Edging
• hedge trimming
• landscaping
•mulching
•yard clean up
• pressure washing

Target Market(s)

Everyone

Contact Information for Business Card

Licensed and insured

Font styles to use
Serif

Colors
59FF00
82FF00
B8FF75
E3FFCB
F4FFEA
F0912C
F2A743
F7CA91
FBE8D2
FDF5EE
EE7325
F08F49
F5BC92
FAE3D3
FDF4ED
EB3D1F
EC4F4E
F09395
F8D3D4
FCEDEE
E54698
E96AAD
F1A4CE
F9D9EA
FCEFF6

```html
<!DOCTYPE html>
<html lang="en">
<head>
<meta charset="utf-8">
<title>Evergrove Yard Service and Beyond LLC — Business Card</title>
<link href="https://fonts.googleapis.com/css2?family=Poppins:wght@400;500;600&display=swap" rel="stylesheet">
<style>
  :root{
    --bg:#e4e4e4;
    --card:#f6f6f6;
    --green:#1f8a12;
    --orange:#ee7325;
    --grey:#6b6b6b;
    --rule:#8a8a8a;
    --ink:#1c1c1c;
  }
  *{box-sizing:border-box;margin:0;padding:0}
  html,body{width:1200px;height:930px;overflow:hidden}
  body{
    background:var(--bg);
    font-family:"Poppins",sans-serif;
    color:var(--ink);
    display:flex;flex-direction:column;align-items:center;justify-content:center;gap:34px;
  }
  .card{
    width:700px;height:400px;background:var(--card);
    box-shadow:0 6px 18px rgba(0,0,0,.12);
    display:flex;flex-direction:column;align-items:center;
  }

  /* brand lockup */
  .brand{margin-top:40px;text-align:center;width:360px}
  .brand-name{
    font-weight:600;color:var(--green);text-transform:uppercase;line-height:1.1;
  }
  .brand-name .primary{display:block;font-size:38px;letter-spacing:2px}
  .brand-name .secondary{display:block;font-size:15.5px;letter-spacing:1.6px;margin-top:2px}
  .brand-tag{
    margin-top:6px;display:flex;align-items:center;gap:10px;
    font-size:11px;letter-spacing:2.5px;text-transform:uppercase;color:var(--grey);white-space:nowrap;
  }
  .brand-tag::before,.brand-tag::after{content:"";flex:1;height:1px;background:var(--rule)}

  /* front */
  .person{margin-top:18px;text-align:center}
  .person-name{font-weight:600;color:var(--green);font-size:19px;letter-spacing:1.5px;text-transform:uppercase;line-height:1.2}
  .person-role{color:var(--orange);font-size:12px;letter-spacing:1.5px;text-transform:uppercase}
  .contact{margin-top:22px;display:flex;align-items:stretch;gap:18px}
  .address{text-align:right;font-size:16px;line-height:1.4}
  .divider{width:1.5px;background:var(--ink)}
  .lines{list-style:none;font-size:16px;line-height:1.4}
  .lines li{display:flex;align-items:center;gap:9px}
  .lines svg{width:15px;height:15px;flex:none}

  /* back */
  .services{
    margin-top:22px;width:600px;height:208px;border:2px solid var(--green);
    padding:18px 34px 18px;
    display:grid;grid-template-columns:1fr 1fr;grid-template-rows:auto 1fr;column-gap:30px;
  }
  .service-list{list-style:none;font-size:16px;line-height:1.45}
  .service-list li::before{content:"• "}
  .service-list.left{grid-column:1;grid-row:1}
  .service-list.right{grid-column:2;grid-row:1 / span 2;align-self:end}
  .services-note{grid-column:1;grid-row:2;margin-top:6px;font-size:16px}
</style>
</head>
<body>

<section class="card card-front">
  <div class="brand">
    <div class="brand-name"><span class="primary">Evergrove</span><span class="secondary">Yard Service and Beyond LLC</span></div>
    <div class="brand-tag">Licensed and insured</div>
  </div>
  <div class="person">
    <div class="person-name">Marcus Hale</div>
    <div class="person-role">Managing Director</div>
  </div>
  <div class="contact">
    <div class="address">87 Willow Bend Road<br>Millbrook<br>30718, Ohio</div>
    <div class="divider"></div>
    <ul class="lines">
      <li>
        <svg viewBox="0 0 24 24" aria-hidden="true"><path fill="var(--orange)" d="M6.6 10.8a15.2 15.2 0 0 0 6.6 6.6l2.2-2.2a1 1 0 0 1 1-.25 11.4 11.4 0 0 0 3.6.57 1 1 0 0 1 1 1V20a1 1 0 0 1-1 1A17 17 0 0 1 3 4a1 1 0 0 1 1-1h3.5a1 1 0 0 1 1 1c0 1.25.2 2.45.57 3.6a1 1 0 0 1-.25 1z"/></svg>
        044-555 010 234
      </li>
      <li>
        <svg viewBox="0 0 24 24" aria-hidden="true"><rect x="2" y="5" width="20" height="14" rx="1.5" fill="var(--orange)"/><path d="M2.5 6l9.5 7 9.5-7" fill="none" stroke="var(--card)" stroke-width="1.6"/></svg>
        info@evergroveyard.com
      </li>
      <li>
        <svg viewBox="0 0 24 24" aria-hidden="true"><circle cx="12" cy="12" r="10" fill="var(--orange)"/><g fill="none" stroke="var(--card)" stroke-width="1.3"><ellipse cx="12" cy="12" rx="4" ry="10"/><path d="M2 12h20M4 7h16M4 17h16"/></g></svg>
        www.evergroveyard.com
      </li>
    </ul>
  </div>
</section>

<section class="card card-back">
  <div class="brand">
    <div class="brand-name"><span class="primary">Evergrove</span><span class="secondary">Yard Service and Beyond LLC</span></div>
    <div class="brand-tag">Licensed and insured</div>
  </div>
  <div class="services">
    <ul class="service-list left">
      <li>Mowing</li>
      <li>Weed eating</li>
      <li>Edging</li>
      <li>Hedge trimming</li>
    </ul>
    <ul class="service-list right">
      <li>Landscaping</li>
      <li>Mulching</li>
      <li>Yard clean up</li>
      <li>Pressure washing</li>
    </ul>
    <p class="services-note">Licensed and Insured</p>
  </div>
</section>

</body>
</html>
```